Forget what you know about corporate well

I need a one-page flies used for print, to embedding in a website, all social media platforms and email.

Target Market(s)

Business

Industry/Entity Type

Health And Wellness

Font styles to use
Serif
Script
Other font styles liked:
• I would like the designers opinion on the font

Colors

Designer to choose colors to be used in the design.

Requirements
Must have
• This is the wording:
• Did you know that 75% of healthcare costs are incurred by preventable diseases? Cardiovascular disease, cancer, and diabetes are the three major causes of rising health care plans and are all preventable.
• Milo and his team have spent decades learning how to increase productivity, reduce absenteeism, and increase employee engagement, all leading to lowering healthcare costs. Together, they have developed a system created to target the masses all while addressing individual needs. Their corporate training challenges helps to engrain positive habits through a carefully curated accountability and reward system.
• How it works:
• Step 1 – evaluate the needs of your business;
• Step 2 – set up individualized workshops based on highest needs;
• Step 3 – create a customized corporate training challenge.
• Why Milo?
• Milo excels at motivational speaking. He is an author, a nutritionist and a professional athlete with a master’s degree in clinical nutrition. He is a teacher of corporate wellness at Fernhollow College and a health coach. Milo has been featured in national magazines, podcasts, and popular fitness websites. Milo’s own health issues put him on a quest to heal himself and others. With twenty-five years of experience and a passion for wellness, he can provide your company with an unforgettable experience.
Nice to have
• I will not give my opinion, I believe that is an insult to the designer. All of the verbiage is above and I attached a plethora of pictures.
Should not have
• No opinion

```html
<!DOCTYPE html>
<html lang="en">
<head>
<meta charset="utf-8">
<title>Milo – Corporate Wellness Flyer</title>
<link href="https://fonts.googleapis.com/css2?family=Open+Sans:ital,wght@0,400;0,700;0,800;1,700&family=Oswald:wght@600&display=swap" rel="stylesheet">
<style>
  :root{
    --paper:#e8e8e8;
    --terracotta:#d0694d;
    --charcoal:#231f20;
    --smoke:rgba(64,60,60,.9);
    --ink:#222;
    --white:#ffffff;
    --blush:#f6d3c5;
  }
  html,body{margin:0;padding:0;overflow:hidden;background:var(--paper);}
  .flyer{
    position:relative;width:855px;height:1200px;overflow:hidden;
    background:var(--paper);
    font-family:"Open Sans",Arial,sans-serif;color:var(--white);
  }
  .flyer > *{position:absolute;}
  .intro-band{left:43px;top:50px;width:771px;height:232px;background:var(--terracotta);}
  .portrait-top{left:590px;top:52px;width:222px;height:188px;
    background:linear-gradient(160deg,#a2553f 0%,#8a4a3a 45%,#3a3030 80%,#1d1b1c 100%);}
  .portrait-main{left:43px;top:282px;width:529px;height:872px;
    background:linear-gradient(180deg,#8d8a88 0%,#6f6b69 45%,#55514f 75%,#3d3a39 100%);}
  .mission-box{left:43px;top:282px;width:535px;height:156px;background:var(--smoke);}
  .spaced{white-space:nowrap;font-size:17.5px;letter-spacing:.19em;line-height:25.2px;}
  .fact{left:50px;top:68px;}
  .fact strong{font-weight:800;font-size:22px;letter-spacing:.15em;}
  .team-line{left:50px;top:209px;letter-spacing:.3em;}
  .team-line em{font-weight:700;font-style:italic;}
  .system{left:50px;top:244px;}
  .increase{left:587px;top:230px;font-family:"Oswald",Impact,sans-serif;font-weight:600;
    font-size:53px;line-height:1;color:var(--blush);letter-spacing:-.01em;}
  .benefits{left:586px;top:282px;width:228px;height:224px;background:var(--charcoal);}
  .benefits-text{left:591px;top:305px;font-size:14.5px;line-height:21.6px;letter-spacing:.2em;}
  .benefits-text b{font-weight:800;}
  .tab{left:585px;width:231px;height:44px;background:var(--terracotta);
    font-weight:800;font-size:16px;letter-spacing:.3em;text-align:center;line-height:44px;}
  .tab-how{top:506px;}
  .tab-why{top:776px;}
  .steps{left:586px;top:550px;width:228px;height:226px;background:var(--charcoal);}
  .steps-text{left:592px;top:558px;font-size:14.5px;line-height:21px;letter-spacing:.16em;}
  .steps-text b{font-weight:800;}
  .rule{left:586px;width:228px;height:3px;background:var(--charcoal);}
  .rule-top{top:833px;}
  .rule-bottom{top:1148px;}
  .why-text{left:590px;top:864px;color:var(--ink);font-size:13.5px;line-height:21.6px;letter-spacing:.06em;white-space:nowrap;}
  .story{left:59px;top:946px;font-size:15.5px;line-height:23.6px;letter-spacing:.08em;white-space:nowrap;}
</style>
</head>
<body>
<main class="flyer">
  <div class="intro-band"></div>
  <div class="portrait-top" role="img" aria-label="Portrait of Milo smiling in a black t-shirt against a red brick wall"></div>
  <div class="portrait-main" role="img" aria-label="Black and white photo of Milo in a jacket standing beside a brick wall"></div>
  <div class="mission-box"></div>

  <p class="spaced fact" style="margin:0">Did you know that <strong>75%</strong> of healthcare costs<br>are incurred by preventable diseases?<br>Cardiovascular disease, cancer, and diabetes<br>are the three major causes of rising health<br>care plans and are all preventable.</p>
  <p class="spaced team-line" style="margin:0">Milo and his team have spent decades learning <em>how to</em></p>
  <p class="spaced system" style="margin:0">Together, they have developed a system<br>created to target the masses all while ad<br>dressing individual needs. Their<br>corporate training challenges helps to<br>engrain positive habits through a<br>carefully curated accountability and<br>reward system.</p>
  <h1 class="increase" style="margin:0">INCREASE</h1>

  <div class="benefits"></div>
  <p class="benefits-text" style="margin:0"><b>PRODUCTIVITY,</b><br>reduce absenteeism<br>and increase<br>employee<br>engagement,<br>all leading to<br>lowering health<br>care costs</p>

  <h2 class="tab tab-how" style="margin:0">HOW IT WORKS</h2>
  <div class="steps"></div>
  <p class="steps-text" style="margin:0"><b>Step 1</b> – evaluate<br>the needs of your<br>business;<br><b>Step 2</b> – set up<br>individualized<br>workshops based<br>on highest needs;<br><b>Step 3</b> – create a<br>customized corporate<br>training challenge.</p>

  <h2 class="tab tab-why" style="margin:0">WHY MILO?</h2>
  <div class="rule rule-top"></div>
  <p class="why-text" style="margin:0">Milo excels at motivational<br>speaking. He is an author,<br>a nutritionist and a<br>professional athlete with a<br>master’s degree in clinical<br>nutrition. He is a teacher of<br>corporate wellness at Fernhollow<br>College and a health coach.<br>Milo has been featured in<br>national magazines,<br>podcasts, and popular fitness<br>websites.</p>
  <div class="rule rule-bottom"></div>

  <p class="story" style="margin:0">Milo’s own health issues put him<br>on a quest to heal himself and<br>others. With twenty-five years of<br>experience and a passion for<br>wellness, he can provide your<br>company with an unforgettable<br>experience.</p>
</main>
</body>
</html>
```